Providing Back Office Solutions to Financial Advisors and Attorney Needs a Business Card Design

Need a Business Card Design that speaks to Financial Advisor and Attorneys. Some of the word that come to mind is Clean/Simple & Futuristic.

Industry/Entity Type

Business

```html
<!DOCTYPE html>
<html lang="en">
<head>
<meta charset="utf-8">
<title>Kalyra Back Office Solutions – Business Card</title>
<link href="https://fonts.googleapis.com/css2?family=Exo+2:wght@500;600&family=Tinos:ital,wght@0,400;1,400&family=Arimo&display=swap" rel="stylesheet">
<style>
  :root {
    --page: #e4e1dc;
    --card: #000000;
    --brand-blue: #0b5aa8;
    --text-light: #e8e8e8;
    --shadow: rgba(0, 0, 0, 0.25);
  }
  html, body {
    margin: 0;
    width: 1200px;
    height: 900px;
    overflow: hidden;
    background: var(--page);
  }
  .canvas {
    position: relative;
    width: 1200px;
    height: 900px;
  }
  .card {
    position: absolute;
    left: 300px;
    width: 600px;
    height: 343px;
    background: var(--card);
    box-shadow: 0 10px 28px var(--shadow);
    overflow: hidden;
  }
  .card--details { top: 70px; }
  .card--brand { top: 487px; }

  .band {
    position: absolute;
    inset: 0;
    width: 600px;
    height: 343px;
  }
  .band-wordmark {
    position: absolute;
    left: 26px;
    top: 46px;
    transform: rotate(30deg);
    transform-origin: top left;
    display: flex;
    align-items: center;
    gap: 8px;
    color: #000;
    white-space: nowrap;
  }
  .band-wordmark .mark-square {
    width: 20px;
    height: 20px;
    background: #000;
  }
  .band-wordmark .name {
    font-family: "Exo 2", sans-serif;
    font-weight: 600;
    font-size: 22px;
    letter-spacing: 2px;
    line-height: 1;
  }
  .band-wordmark .tagline {
    font-family: "Exo 2", sans-serif;
    font-weight: 600;
    font-size: 9px;
    letter-spacing: 0.5px;
    margin-top: 2px;
  }

  .contact {
    position: absolute;
    right: 30px;
    top: 36px;
    text-align: right;
    color: var(--text-light);
    font-family: "Arimo", sans-serif;
    font-size: 13px;
    line-height: 1.45;
  }
  .contact .person {
    font-family: "Tinos", serif;
    font-style: italic;
    color: var(--brand-blue);
    font-size: 22px;
    line-height: 1.1;
  }
  .contact .role {
    font-family: "Tinos", serif;
    font-size: 11px;
    margin-bottom: 14px;
  }

  .brand-lockup {
    position: absolute;
    left: 50%;
    top: 50%;
    transform: translate(-50%, -50%);
    display: flex;
    align-items: center;
    gap: 16px;
    color: var(--brand-blue);
  }
  .brand-lockup .mark-square {
    width: 64px;
    height: 64px;
    background: var(--brand-blue);
  }
  .brand-lockup .divider {
    width: 2px;
    height: 96px;
    background: var(--brand-blue);
  }
  .brand-lockup .name {
    font-family: "Exo 2", sans-serif;
    font-weight: 600;
    font-size: 58px;
    letter-spacing: 4px;
    line-height: 1;
  }
  .brand-lockup .tagline {
    font-family: "Exo 2", sans-serif;
    font-weight: 600;
    font-size: 17px;
    letter-spacing: 0.8px;
    margin-top: 6px;
  }
</style>
</head>
<body>
<main class="canvas">
  <section class="card card--details">
    <svg class="band" viewBox="0 0 600 343" aria-hidden="true">
      <polygon points="0,20 0,130 430,343 560,343" fill="var(--brand-blue)"/>
      <polygon points="0,130 0,138 414,343 430,343" fill="#000"/>
    </svg>
    <div class="band-wordmark">
      <div class="mark-square"></div>
      <div>
        <div class="name">KALYRA</div>
        <div class="tagline">BACK OFFICE SOLUTIONS</div>
      </div>
    </div>
    <div class="contact">
      <div class="person">Jane Doe</div>
      <div class="role">Chief Executive Officer</div>
      <div>Suite 64, 123 Street Road</div>
      <div>Tel: 123 456 789</div>
      <div>Mob: 1245 678 910</div>
      <div>Email: yourname@yourcompany.com</div>
      <div>www.yourcompany.com</div>
    </div>
  </section>

  <section class="card card--brand">
    <div class="brand-lockup">
      <div class="mark-square"></div>
      <div class="divider"></div>
      <div>
        <div class="name">KALYRA</div>
        <div class="tagline">BACK OFFICE SOLUTIONS</div>
      </div>
    </div>
  </section>
</main>
</body>
</html>
```